Film Festival Poster Design Project

The 5th Annual Harwell Open Screen Festival will be taking place on November 12th in Wales at the Larkmoor Cinema, Newport.

It is an all day event and there will be an eclectic mix of films on show.

Target Market(s)

Students 18-25

Industry/Entity Type

Festival

Requirements
Must have
• Title: 5th Harwell Open Screen Festival

Date: Saturday 12th November 2011

Place: Larkmoor Theatre & Cinema, Newport, Wales

Must include the text: BUY TICKETS ONLINE AT WWW.REELGATHERHALL.EXAMPLE

Sponsors & Festival Logo's must be included.
Nice to have
• As the festival is based in Wales, it would be nice to have a slightly Welsh tone to the poster, or a British feel.

```html
<!DOCTYPE html>
<html lang="en">
<head>
<meta charset="utf-8">
<title>5th Harwell Open Screen Festival</title>
<link rel="stylesheet" href="https://fonts.googleapis.com/css2?family=Anton&family=Archivo+Black&family=Gelasio:wght@400;700&family=Montserrat:wght@600&display=swap">
<style>
  :root {
    --festival-red: #e0262a;
    --ink-grey: #3b3b3b;
    --band-grey: #4a4a4a;
    --band-grey-light: #6b6b6b;
    --paper: #ffffff;
  }
  html, body {
    margin: 0;
    padding: 0;
    overflow: hidden;
    background: var(--paper);
  }
  .poster {
    position: relative;
    width: 941px;
    height: 1200px;
    overflow: hidden;
    background: var(--paper);
    font-family: "Gelasio", Georgia, serif;
  }
  .poster-backdrop {
    position: absolute;
    inset: 0;
  }
  .festival-title {
    position: absolute;
    top: 110px;
    right: 40px;
    margin: 0;
    text-align: right;
    font-family: "Anton", "Impact", sans-serif;
    font-weight: 400;
    font-size: 104px;
    line-height: 132px;
    letter-spacing: 2px;
    color: var(--festival-red);
    -webkit-text-stroke: 3px var(--paper);
    paint-order: stroke fill;
  }
  .festival-title span { display: block; }
  .sponsor {
    position: absolute;
    right: 40px;
    top: 560px;
    display: flex;
    align-items: center;
    gap: 14px;
  }
  .sponsor-dot {
    width: 22px;
    height: 22px;
    border-radius: 50%;
    background: var(--paper);
  }
  .sponsor-name {
    font-family: "Gelasio", Georgia, serif;
    font-weight: 700;
    font-size: 40px;
    line-height: 1;
    color: var(--paper);
  }
  .ticket-call {
    position: absolute;
    left: 0;
    width: 941px;
    top: 860px;
    text-align: center;
    margin: 0;
    font-family: "Archivo Black", "Arial Black", sans-serif;
    font-size: 63px;
    line-height: 1;
    color: var(--festival-red);
    letter-spacing: 0.5px;
  }
  .ticket-url {
    position: absolute;
    left: 0;
    width: 941px;
    top: 930px;
    text-align: center;
    margin: 0;
    font-family: "Archivo Black", "Arial Black", sans-serif;
    font-size: 41px;
    line-height: 1;
    color: var(--ink-grey);
  }
  .event-date {
    position: absolute;
    right: 20px;
    top: 1005px;
    margin: 0;
    font-size: 29px;
    color: var(--ink-grey);
  }
  .event-date .label { color: var(--festival-red); }
  .event-place {
    position: absolute;
    left: 18px;
    top: 1056px;
    color: var(--paper);
  }
  .event-place h2 {
    margin: 0 0 4px;
    font-family: "Montserrat", Arial, sans-serif;
    font-weight: 600;
    font-size: 29px;
    line-height: 1.1;
  }
  .event-place ul {
    margin: 0;
    padding: 0 0 0 10px;
    list-style: none;
    font-size: 24px;
    line-height: 33px;
  }
  .event-place li::before {
    content: "";
    display: inline-block;
    width: 7px;
    height: 7px;
    border-radius: 50%;
    background: var(--paper);
    margin-right: 6px;
    vertical-align: middle;
    position: relative;
    top: -3px;
  }
</style>
</head>
<body>
<main class="poster">
  <svg class="poster-backdrop" width="941" height="1200" viewBox="0 0 941 1200">
    <defs>
      <linearGradient id="sceneTone" x1="0" y1="0" x2="0" y2="1">
        <stop offset="0" stop-color="#9c968a"/>
        <stop offset="0.22" stop-color="#c9b48c"/>
        <stop offset="0.42" stop-color="#8a7d5a"/>
        <stop offset="0.6" stop-color="#5c5a2e"/>
        <stop offset="0.78" stop-color="#6e8a32"/>
        <stop offset="1" stop-color="#7da63b"/>
      </linearGradient>
    </defs>
    <rect class="festival-photo" role="img" aria-label="Photograph of a stone castle keep on a grassy mound framed by autumn trees" x="0" y="0" width="941" height="860" fill="url(#sceneTone)"/>
    <path class="white-sweep" d="M0 845 C 160 820 300 760 420 728 C 560 694 760 690 941 682 L 941 1200 L 0 1200 Z" fill="#ffffff"/>
    <path class="place-band-shade" d="M0 1052 L 430 1052 C 470 1060 520 1120 600 1200 L 0 1200 Z" fill="#6b6b6b"/>
    <path class="place-band" d="M0 1045 L 410 1045 C 450 1050 500 1110 560 1200 L 0 1200 Z" fill="#4a4a4a"/>
  </svg>

  <h1 class="festival-title">
    <span>5th Harwell</span>
    <span>Open Screen</span>
    <span>Festival</span>
  </h1>

  <div class="sponsor">
    <span class="sponsor-dot"></span>
    <span class="sponsor-name">Tallowby Films</span>
  </div>

  <p class="ticket-call">BUY TICKETS ONLINE AT</p>
  <p class="ticket-url">WWW.REELGATHERHALL.EXAMPLE</p>

  <p class="event-date"><span class="label">Date:</span> Saturday 12th November 2011</p>

  <section class="event-place">
    <h2>Place:</h2>
    <ul>
      <li>Larkmoor Theatre &amp; Cinema</li>
      <li>Newport</li>
      <li>Wales</li>
    </ul>
  </section>
</main>
</body>
</html>
```